Website Design for Quellon Music Services

Quellon Music Services offers a radically different business model for getting the business support needed to take artists' music career to the next level. QMS offers all of the services of a traditional record label, but without taking royalties or creative

```html
<!DOCTYPE html>
<html lang="en">
<head>
<meta charset="utf-8">
<title>Quellon Music Services</title>
<link href="https://fonts.googleapis.com/css2?family=PT+Sans:wght@400;700&display=swap" rel="stylesheet">
<style>
:root{
  --header-bg:#1b1b1b;
  --page-bg:#141414;
  --footer-bg:#1f1f1f;
  --footer-base:#0f0f0f;
  --panel-bg:#e7e7e7;
  --white:#ffffff;
  --brand-red:#d0171d;
  --tagline-red:#c8242a;
  --button-red:#c4141a;
  --button-blue:#2a8fd8;
  --button-black:#151515;
  --muted:#8a8a8a;
  --label:#5a5a5a;
  --separator:#555555;
}
*{box-sizing:border-box;margin:0;padding:0}
html,body{width:1200px;height:949px;overflow:hidden}
body{position:relative;background:var(--page-bg);font-family:"PT Sans",Arial,sans-serif;color:var(--white)}
a{text-decoration:none}

.site-header{position:absolute;left:0;top:0;width:1200px;height:93px;background:var(--header-bg)}
.brand{position:absolute;left:111px;top:16px;display:flex;align-items:center;gap:10px}
.brand-mark{width:16px;height:16px;background:var(--white)}
.brand-name{font-size:22px;font-weight:700;color:var(--white);line-height:24px;width:170px}
.tagline{position:absolute;left:325px;top:12px;font-size:18px;color:var(--tagline-red);white-space:nowrap}
.social{position:absolute;display:flex;gap:14px}
.social span{width:27px;height:27px;border-radius:50%;background:#3a3a3a;display:block}
.site-header .social{left:1011px;top:12px}
.main-nav{position:absolute;right:136px;top:62px;display:flex;font-size:16px;font-weight:700}
.main-nav a{color:var(--white);padding:0 14px;border-left:1px solid var(--separator);line-height:24px}
.main-nav a:first-child{border-left:none;padding-left:0}
.main-nav a:last-child{padding-right:0}

.hero{position:absolute;left:0;top:93px;width:1200px;height:560px}
.hero-media{position:absolute;inset:0;background:linear-gradient(90deg,#d8143c 0%,#c41f8a 30%,#5b2fc8 55%,#1f49c8 75%,#1b5fd8 100%)}
.hero-title{position:absolute;left:409px;top:128px;width:388px;height:147px;background:rgba(20,20,40,.55);font-size:50px;font-weight:700;line-height:48px;padding:20px 0 0 32px;text-transform:uppercase}
.hero-title span{display:block}
.hero-title span+span{padding-left:82px}
.hero-sub{position:absolute;left:289px;top:314px;width:662px;height:56px;background:rgba(10,10,20,.6);font-size:20px;font-weight:700;line-height:56px;padding-left:8px;white-space:nowrap}
.btn{position:absolute;display:flex;align-items:center;justify-content:center;font-weight:700;font-size:18px;color:var(--white);border-radius:7px;text-transform:uppercase;white-space:nowrap}
.hero .btn{left:511px;top:388px;width:162px;height:42px;background:var(--button-red)}

.features{position:absolute;left:109px;top:600px;width:982px;height:237px;background:var(--panel-bg)}
.feature{position:absolute;top:0;width:305px}
.feature h3{position:absolute;top:24px;font-size:13px;font-weight:700;color:var(--label);text-transform:uppercase;white-space:nowrap}
.feature-card{position:absolute;top:49px;width:305px;height:159px}
.feature-media{position:absolute;inset:0}
.feature-text{position:absolute;font-size:18px;font-weight:700;line-height:21px}
.feature--services{left:15px}
.feature--services .feature-media{background:linear-gradient(90deg,#e2e2e2,#9a9a9a)}
.feature--services .feature-text{left:8px;top:8px;width:262px;color:var(--brand-red)}
.feature--services .btn{left:131px;top:104px;width:161px;height:43px;background:var(--button-black)}
.feature--start{left:338px}
.feature--start .feature-media{background:linear-gradient(90deg,#3a3a3a,#111111)}
.feature--start .feature-text{left:148px;top:18px;width:150px;text-transform:uppercase}
.feature--start .btn{left:133px;top:107px;width:161px;height:40px;background:var(--button-red)}
.feature--talk{left:659px}
.feature--talk .feature-media{background:linear-gradient(90deg,#2a1a10,#8a5a30 55%,#3a2a1c)}
.feature--talk .feature-text{left:9px;top:6px;width:272px;text-transform:uppercase}
.feature--talk .btn{left:25px;top:107px;width:251px;height:40px;background:var(--button-blue)}

.site-footer{position:absolute;left:0;top:860px;width:1200px;height:60px;background:var(--footer-bg)}
.footer-links{position:absolute;left:119px;top:20px;display:flex;font-size:14px}
.footer-links a{color:var(--muted);padding:0 8px;border-left:1px solid #4a4a4a;line-height:16px}
.footer-links a:first-child{border-left:none;padding-left:0}
.site-footer .social{left:1011px;top:15px}
.footer-base{position:absolute;left:0;top:920px;width:1200px;height:29px;background:var(--footer-base)}
</style>
</head>
<body>
<header class="site-header">
  <div class="brand"><span class="brand-mark"></span><span class="brand-name">Quellon Music Services</span></div>
  <p class="tagline">The Only Full-Service Partner for Musicians</p>
  <div class="social" aria-label="Social links"><span></span><span></span></div>
  <nav class="main-nav">
    <a href="#">HOW WE HELP</a>
    <a href="#">PRICING</a>
    <a href="#">WHERE TO START</a>
  </nav>
</header>

<section class="hero">
  <div class="hero-media" role="img" aria-label="Collage of musicians performing on stage in red, pink and blue light"></div>
  <h1 class="hero-title"><span>Your Music,</span><span>Your Way</span></h1>
  <p class="hero-sub">Services and support that help you take your music to the next level.</p>
  <a class="btn" href="#">Learn More</a>
</section>

<section class="features">
  <div class="feature feature--services">
    <h3>Services</h3>
    <div class="feature-card">
      <div class="feature-media" role="img" aria-label="Sheet music close-up"></div>
      <p class="feature-text">Services and support that help you take your music to the next level.</p>
      <a class="btn" href="#">Learn More</a>
    </div>
  </div>
  <div class="feature feature--start">
    <h3>Get Started Now</h3>
    <div class="feature-card">
      <div class="feature-media" role="img" aria-label="Turntable with a record"></div>
      <p class="feature-text">Ready to start selling your music today?</p>
      <a class="btn" href="#">Sign Up Now</a>
    </div>
  </div>
  <div class="feature feature--talk">
    <h3>Talk to Someone</h3>
    <div class="feature-card">
      <div class="feature-media" role="img" aria-label="Hands playing an acoustic guitar"></div>
      <p class="feature-text">Want to learn more about our music services?</p>
      <a class="btn" href="#">Speak with an Advisor</a>
    </div>
  </div>
</section>

<footer class="site-footer">
  <nav class="footer-links">
    <a href="#">Home</a>
    <a href="#">About Us</a>
    <a href="#">Contact Us,</a>
    <a href="#">Privacy Policy</a>
    <a href="#">Terms of Use</a>
  </nav>
  <div class="social" aria-label="Social links"><span></span><span></span></div>
</footer>
<div class="footer-base"></div>
</body>
</html>
```